Fern Lattice Logo, Icons and web design

Looking for a new logo for the Sprout Oracle, and a set of 12-15 icons and color scheme (and a few sample pages) to include some creative, but clean and professional content boxes. The current site is http://www.fernlattice-example.com. We would like to see logo variants - both based on the current design, as well as some new creative options.
Fern Lattice is a SaaS website designed for the green industry participants who want to save trees during construction or other land disturbances (landscape architects, builders/developers, architects, homeowners). It features a patented algorithm to predict tree survival. We also offer the Sprout Oracle to find the best plant for the planting location.

We would like to see a page with embedded video for our promotional and tutorial videos.

Specifically we would to see icons for two services:

Fern Lattice: A root plotting tree survival prediction tool
https://www.fernlattice-example.com/how-bark-keeper-works

Our Sprout Oracle: https://www.fernlattice-example.com/how-sprout-oracle-works
The current site is based on a twitter bootstrap 4.0 template, so this is strongly preferred.

Target Market(s)

Landscape architects, builders and developer as well as municipal tree planning and preservation specialists.

Coding

Coded - Design and coding required

Number of Pages Required

4 page

Font styles to use
Sans Serif

```html
<!DOCTYPE html>
<html lang="en">
<head>
<meta charset="utf-8">
<title>Fern Lattice — Tree Preservation</title>
<link rel="stylesheet" href="https://fonts.googleapis.com/css2?family=Heebo:wght@300;800;900&family=Merriweather:wght@700&family=Raleway:wght@700;800&display=swap">
<style>
  :root {
    --brand-green: #3f6b3a;
    --button-green: #2f5a2a;
    --nav-ink: #1c1c1c;
    --nav-bg: #ffffff;
    --hero-text: #ffffff;
    --forest-deep: #1f2c14;
    --forest-mid: #4a5e22;
    --forest-moss: #7a8a2a;
    --forest-amber: #8a6a2a;
  }
  * { box-sizing: border-box; margin: 0; padding: 0; }
  html, body {
    width: 1200px;
    height: 575px;
    overflow: hidden;
    background: var(--nav-bg);
  }
  .page {
    position: relative;
    width: 1200px;
    height: 575px;
    overflow: hidden;
  }
  .site-header {
    position: absolute;
    top: 0; left: 0;
    width: 1200px;
    height: 61px;
    background: var(--nav-bg);
    display: flex;
    align-items: center;
    justify-content: space-between;
    padding: 0 110px 0 112px;
    z-index: 2;
  }
  .brand {
    display: flex;
    align-items: center;
    gap: 9px;
    text-decoration: none;
  }
  .brand-dot {
    width: 34px;
    height: 34px;
    border-radius: 50%;
    background: var(--brand-green);
  }
  .brand-name {
    font-family: "Merriweather", Georgia, serif;
    font-weight: 700;
    font-size: 25px;
    color: var(--brand-green);
    letter-spacing: 0.2px;
  }
  .main-nav {
    display: flex;
    gap: 23px;
    list-style: none;
  }
  .main-nav a {
    font-family: "Raleway", Arial, sans-serif;
    font-weight: 800;
    font-size: 13px;
    color: var(--nav-ink);
    text-decoration: none;
    display: flex;
    align-items: center;
    gap: 3px;
  }
  .main-nav svg { width: 8px; height: 8px; }
  .hero {
    position: absolute;
    top: 61px; left: 0;
    width: 1200px;
    height: 514px;
  }
  .hero-backdrop {
    position: absolute;
    inset: 0;
    background:
      radial-gradient(ellipse 40% 45% at 55% 30%, rgba(140,150,60,0.55), transparent 70%),
      radial-gradient(ellipse 35% 30% at 88% 25%, rgba(150,120,60,0.5), transparent 70%),
      radial-gradient(ellipse 50% 35% at 50% 90%, rgba(120,130,40,0.6), transparent 70%),
      linear-gradient(180deg, var(--forest-deep) 0%, var(--forest-mid) 45%, var(--forest-moss) 75%, var(--forest-amber) 100%);
  }
  .hero-backdrop::after {
    content: "";
    position: absolute;
    inset: 0;
    background: rgba(0,0,0,0.18);
  }
  .hero-content {
    position: absolute;
    inset: 0;
    display: flex;
    flex-direction: column;
    align-items: center;
    color: var(--hero-text);
    font-family: "Heebo", Arial, sans-serif;
  }
  .hero-kicker {
    margin-top: 222px;
    font-weight: 300;
    font-size: 29px;
    line-height: 34px;
    letter-spacing: 0.3px;
  }
  .hero-title {
    margin-top: 8px;
    font-weight: 900;
    font-size: 60px;
    line-height: 66px;
    letter-spacing: 0.5px;
  }
  .hero-actions {
    margin-top: 22px;
    display: flex;
    gap: 12px;
  }
  .btn {
    height: 41px;
    display: inline-flex;
    align-items: center;
    justify-content: center;
    font-family: "Raleway", Arial, sans-serif;
    font-weight: 800;
    font-size: 13px;
    color: var(--hero-text);
    text-decoration: none;
  }
  .btn-primary {
    width: 151px;
    background: var(--button-green);
  }
  .btn-outline {
    width: 118px;
    border: 2px solid var(--button-green);
  }
</style>
</head>
<body>
<div class="page">
  <header class="site-header">
    <a class="brand" href="http://www.fernlattice-example.com">
      <span class="brand-dot"></span>
      <span class="brand-name">Fern Lattice</span>
    </a>
    <nav>
      <ul class="main-nav">
        <li><a href="#">OUR PRODUCTS
          <svg viewBox="0 0 10 10"><path d="M1.5 3 L5 6.5 L8.5 3" fill="none" stroke="currentColor" stroke-width="2"/></svg>
        </a></li>
        <li><a href="#">TUTORIAL</a></li>
        <li><a href="#">SEE DEMO</a></li>
        <li><a href="#">CONTACT</a></li>
      </ul>
    </nav>
  </header>

  <section class="hero">
    <div class="hero-backdrop" role="img" aria-label="Photograph of a sunlit conifer forest with mossy ground and a fallen tree"></div>
    <div class="hero-content">
      <p class="hero-kicker">TAKE THE UNCERTAINTY</p>
      <h1 class="hero-title">OUT OF TREE PRESERVATION</h1>
      <div class="hero-actions">
        <a class="btn btn-primary" href="#">START FREE TRIAL</a>
        <a class="btn btn-outline" href="#">KNOW MORE</a>
      </div>
    </div>
  </section>
</div>
</body>
</html>
```